Flyer Design Project - law firm

I need a design for an advertising flyer for my law firm.
Ideally the size of the document will be one page A4.
I have attached a copy of the logo. I would like the lettering for 'Marwood Legal' to be all the same size, rather than the 'S' and 'L' being slightly larger
The flyer must include the text below:
Wills
Anyone who owns property or investments or has family obligations should have a Will to ensure that their assets are distributed in accordance with their wishes and that their children are cared for by the guardians of their choosing. Without a Will, these vital decisions are determined by the government or the courts of the State or Territory which you lived in at the time of your death.
Marwood Legal can assist you in the preparation of a legal will tailored to your particular circumstances to ensure that your wishes are followed.
We are offering Tollbeck- Crane Harbour clients a free discussion of their will requirements and a heavily discounted standard wills package of
$330.00* for a single will
$550.00* for couples wills
These prices are only valid prior to your conveyancing settlement for standard wills (e.g. not including a testamentary trust or other complications.
Please contact us on or provide Tollbeck Crane Harbour with authority for us to contact you today.
Updates
Hi All,
I have posted a copy of the proposed logo. Please note that I need the wording of 'Marwood Legal' to all be the same size, rather than the 'S' and 'L' being slightly larger.
If you require anything further please let me know.
Thanks
I have added copies of the logo in ups format,
If you require anything further please let know.
Thanks for your assistance.

```html
<!DOCTYPE html>
<html lang="en">
<head>
<meta charset="utf-8">
<title>Marwood Legal – Wills</title>
<link rel="stylesheet" href="https://fonts.googleapis.com/css2?family=Gelasio:wght@400&family=PT+Sans:wght@400&display=swap">
<style>
  :root {
    --navy-deep: #1c2474;
    --navy: #2c3590;
    --navy-light: #3a44a6;
    --brand-yellow: #f6d41c;
    --text-white: #ffffff;
    --btn-top: #f8d81c;
    --btn-bottom: #e2582a;
    --metal-light: #c9ccd3;
    --metal-mid: #8d939d;
    --metal-dark: #3b3f47;
  }
  * { margin: 0; padding: 0; box-sizing: border-box; }
  html, body { width: 848px; height: 1200px; overflow: hidden; }
  body { font-family: "PT Sans", Arial, sans-serif; color: var(--text-white); }

  .flyer {
    position: relative;
    width: 848px;
    height: 1200px;
    overflow: hidden;
    background:
      radial-gradient(ellipse at 70% 45%, rgba(80,90,190,0.55), transparent 60%),
      linear-gradient(180deg, var(--navy) 0%, var(--navy-light) 45%, var(--navy-deep) 100%);
  }
  .backdrop-photo {
    position: absolute; inset: 0;
    background: radial-gradient(ellipse at 80% 60%, rgba(20,26,90,0.5), transparent 55%);
  }

  .brand-name {
    position: absolute; top: 22px; left: 0; width: 100%;
    text-align: center;
    font-family: "Gelasio", Georgia, serif;
    font-weight: 400;
    font-size: 76px;
    line-height: 1;
    color: var(--brand-yellow);
  }
  .section-title {
    position: absolute; top: 148px; left: 0; width: 100%;
    text-align: center; font-size: 18px;
  }
  .copy {
    position: absolute; left: 40px; width: 768px;
    text-align: center; font-size: 19.5px; line-height: 28px;
  }
  .copy-intro { top: 204px; }
  .copy-service { top: 390px; }
  .copy-offer { top: 490px; }
  .copy-terms { top: 664px; left: 46px; width: 760px; text-align: justify; text-align-last: center; }

  .price {
    position: absolute; top: 580px; width: 356px; height: 75px;
    border-radius: 12px;
    border: 1px solid rgba(255,255,255,0.7);
    background: linear-gradient(180deg, var(--btn-top) 0%, #f0a024 50%, var(--btn-bottom) 100%);
    text-align: center;
    font-family: "Gelasio", Georgia, serif;
  }
  .price-single { left: 430px; }
  .price-couples { left: 52px; }
  .price-amount { display: block; font-size: 32px; line-height: 34px; margin-top: 4px; }
  .price-label { display: block; font-size: 22px; line-height: 28px; }

  .feature-photo { position: absolute; left: 0; top: 0; width: 848px; height: 1200px; }
</style>
</head>
<body>
<main class="flyer">
  <div class="backdrop-photo" role="img" aria-label="Faint photograph of a judge's gavel in blue tones"></div>

  <h1 class="brand-name">marwood legal</h1>
  <h2 class="section-title">Wills</h2>

  <p class="copy copy-intro">Anyone who owns property or investments or has family obligations should have a Will to ensure that their assets are distributed in accordance with their wishes and that their children are cared for by the guardians of their choosing. Without a Will, these vital decisions are determined by the government or the courts of the State or Territory which you lived in at the time of your death.</p>

  <p class="copy copy-service">Marwood Legal can assist you in the preparation of a legal will tailored to your particular circumstances to ensure that your wishes are followed.</p>

  <p class="copy copy-offer">We are offering Tollbeck Crane Harbour clients a free discussion of their will requirements and a heavily discounted standard wills package of</p>

  <div class="price price-couples">
    <span class="price-amount">$550.00*</span>
    <span class="price-label">for couples wills</span>
  </div>
  <div class="price price-single">
    <span class="price-amount">$330.00*</span>
    <span class="price-label">for sngle will</span>
  </div>

  <p class="copy copy-terms">These prices are only valid prior to your conveyancing settlement for standard wills (e.g. not including a testamentary trust or other complications.</p>

  <svg class="feature-photo" viewBox="0 0 848 1200" role="img" aria-label="Photograph of a brushed metal plaque with raised letters reading The Law, fixed with rivets">
    <defs>
      <linearGradient id="metal" x1="0" y1="0" x2="1" y2="1">
        <stop offset="0" stop-color="var(--metal-light)"/>
        <stop offset="0.5" stop-color="var(--metal-mid)"/>
        <stop offset="1" stop-color="var(--metal-dark)"/>
      </linearGradient>
    </defs>
    <path d="M0,960 C20,880 45,795 125,782 C250,768 385,805 520,792 C650,780 700,742 760,722 C802,708 832,732 848,762 L848,1200 L0,1200 Z" fill="url(#metal)"/>
  </svg>
</main>
</body>
</html>
```